Business card design needed

A laid back coffee shop that has a great feel, that becomes a bar and grill at night. We are also wanting to cater for functions etc.
The business itself is painted dark blue/charcoal and has red doors.
Would like a logo that will be recognised when seen.

Industry/Entity Type

Coffee Shop

Contact Information for Business Card

The Lantern Coffee Bar & Grill
14b Wattlebrook St
Kelmarra NSW 2318
Ph. 02 4817 6293

Logo Text

Logo styles of interest
Emblem Logo
Abstract Logo
Wordmark Logo
Requirements
Must have
• A loyalty card on the back with 2 rows of 7 stamp spaces and a place to write a name and phone number (for a draw)

```html
<!DOCTYPE html>
<html lang="en">
<head>
<meta charset="utf-8">
<title>The Lantern Coffee Bar &amp; Grill – Business Card</title>
<link href="https://fonts.googleapis.com/css2?family=Cabin:wght@400;600&display=swap" rel="stylesheet">
<style>
  :root {
    --page-bg: #e9e7e3;
    --navy-deep: #14173a;
    --navy-mid: #1c2a6e;
    --navy-glow: #1f3f9c;
    --ink-light: #ffffff;
    --ink-soft: #dfe3f0;
    --brand-silver: #d9dce3;
    --cup-cream: #e8e6e1;
    --coffee-brown: #8a5a2b;
    --field-white: #ffffff;
  }
  * { box-sizing: border-box; margin: 0; padding: 0; }
  html, body {
    width: 1200px; height: 900px; overflow: hidden;
    background: var(--page-bg);
    font-family: "Cabin", "Gill Sans", sans-serif;
  }
  .sheet {
    width: 1200px; height: 900px;
    display: flex; flex-direction: column; align-items: center; justify-content: center;
    gap: 56px;
  }
  .card {
    position: relative;
    width: 630px; height: 360px;
    border-radius: 4px;
    overflow: hidden;
    background: radial-gradient(ellipse at 58% 45%, var(--navy-glow) 0%, var(--navy-mid) 38%, var(--navy-deep) 100%);
    box-shadow: 0 10px 28px rgba(0,0,0,.28);
    color: var(--ink-light);
  }

  /* brand name */
  .brand { position: absolute; display: flex; align-items: center; gap: 12px; }
  .brand-name {
    font-weight: 600; color: var(--brand-silver);
    line-height: 1.05;
  }
  .brand-dot { width: 22px; height: 22px; border-radius: 50%; background: var(--brand-silver); flex: none; }

  /* front */
  .card-front .brand { left: 60px; top: 58px; }
  .card-front .brand-name { font-size: 40px; width: 330px; }
  .contact {
    position: absolute; right: 44px; top: 150px; text-align: right;
  }
  .employee-name { font-size: 22px; letter-spacing: .3px; }
  .employee-title { font-size: 18px; letter-spacing: 1px; color: var(--ink-soft); margin-bottom: 12px; }
  .contact-line { font-size: 15px; line-height: 1.45; color: var(--ink-soft); }
  .cup-art {
    position: absolute; left: 90px; bottom: 24px; width: 150px; height: 150px;
    border-radius: 10px;
    background: linear-gradient(180deg, rgba(138,90,43,.55) 0%, rgba(232,230,225,.85) 60%, rgba(138,90,43,.6) 100%);
  }

  /* back */
  .card-back .brand { right: 36px; top: 34px; flex-direction: row-reverse; }
  .card-back .brand-name { font-size: 28px; width: 240px; text-align: right; }
  .stamp-grid {
    position: absolute; left: 72px; top: 120px;
    display: grid; grid-template-columns: repeat(7, 44px); gap: 14px 16px;
  }
  .stamp { width: 44px; height: 40px; border-radius: 8px; background: var(--field-white); }
  .entry { position: absolute; left: 40px; display: flex; align-items: center; gap: 10px; }
  .entry-label { font-size: 15px; width: 58px; text-align: right; }
  .entry-line { width: 330px; height: 22px; border-radius: 4px; background: var(--field-white); }
  .entry-name { top: 238px; }
  .entry-phone { top: 272px; }
  .cup-art-small {
    position: absolute; right: 50px; bottom: 22px; width: 130px; height: 110px;
    border-radius: 10px;
    background: linear-gradient(180deg, rgba(138,90,43,.45) 0%, rgba(232,230,225,.8) 65%, rgba(138,90,43,.55) 100%);
  }
</style>
</head>
<body>
  <main class="sheet">
    <section class="card card-front" aria-label="Business card front">
      <div class="brand">
        <span class="brand-name">The Lantern Coffee Bar &amp; Grill</span>
        <span class="brand-dot"></span>
      </div>
      <div class="contact">
        <p class="employee-name">Employee Name</p>
        <p class="employee-title">Title</p>
        <p class="contact-line">14b Wattlebrook St Kelmarra NSW 2318</p>
        <p class="contact-line">Ph. 02 4817 6293</p>
      </div>
      <div class="cup-art" role="img" aria-label="Illustration of a steaming white coffee cup on a saucer"></div>
    </section>

    <section class="card card-back" aria-label="Loyalty card back">
      <div class="brand">
        <span class="brand-name">The Lantern Coffee Bar &amp; Grill</span>
        <span class="brand-dot"></span>
      </div>
      <div class="stamp-grid" aria-label="Loyalty stamp spaces">
        <span class="stamp"></span><span class="stamp"></span><span class="stamp"></span><span class="stamp"></span><span class="stamp"></span><span class="stamp"></span><span class="stamp"></span>
        <span class="stamp"></span><span class="stamp"></span><span class="stamp"></span><span class="stamp"></span><span class="stamp"></span><span class="stamp"></span><span class="stamp"></span>
      </div>
      <div class="entry entry-name">
        <span class="entry-label">Name</span><span class="entry-line"></span>
      </div>
      <div class="entry entry-phone">
        <span class="entry-label">Ph. No.</span><span class="entry-line"></span>
      </div>
      <div class="cup-art-small" role="img" aria-label="Illustration of a steaming coffee cup on a saucer"></div>
    </section>
  </main>
</body>
</html>
```